Criação de Power Point Slide Mestre para Outros
A empresa queria:
" Nossa empresa aloca funcionários para realizar a limpeza de empresas e condomínios, além de controle de portaria. Também realizamos a administração do condomínio. "

```html
<!DOCTYPE html>
<html lang="pt-BR">
<head>
<meta charset="UTF-8">
<title>Slide Mestre – Clarvia Serviços</title>
<link href="https://fonts.googleapis.com/css2?family=Open+Sans:ital,wght@0,400;0,600;0,700;1,400;1,600&display=swap" rel="stylesheet">
<style>
  :root {
    --navy: #142a47;
    --orange: #f28c1e;
    --white: #ffffff;
    --ink: #1d2330;
    --page: #eceef1;
    --photo-a: #e9ecef;
    --photo-b: #c7ccd3;
  }
  html, body {
    margin: 0;
    width: 1200px;
    height: 1200px;
    overflow: hidden;
    background: var(--page);
    font-family: "Open Sans", Arial, sans-serif;
  }
  .slide {
    position: absolute;
    left: 60px;
    top: 262px;
    width: 1080px;
    height: 608px;
    background: var(--white);
    box-shadow: 0 6px 24px rgba(0,0,0,0.12);
    overflow: hidden;
  }
  .slide-header {
    position: absolute;
    left: 0; top: 0;
    width: 100%;
    height: 112px;
    background: var(--navy);
  }
  .slide-title {
    position: absolute;
    left: 42px; top: 16px;
    margin: 0;
    color: var(--orange);
    font-size: 44px;
    font-weight: 700;
    letter-spacing: -0.5px;
  }
  .slide-subtitle {
    position: absolute;
    left: 44px; top: 70px;
    margin: 0;
    color: var(--white);
    font-size: 24px;
    font-style: italic;
  }
  .brand {
    position: absolute;
    right: 44px; top: 40px;
    display: flex;
    align-items: center;
    gap: 10px;
    color: var(--white);
    font-size: 20px;
    font-weight: 600;
    letter-spacing: 2px;
    text-transform: uppercase;
  }
  .brand-dot {
    width: 14px; height: 14px;
    background: var(--orange);
    border-radius: 50%;
  }
  .slide-body {
    position: absolute;
    left: 90px; top: 178px;
    width: 520px;
    margin: 0;
    color: var(--ink);
    font-size: 17px;
    line-height: 1.62;
    text-align: center;
  }
  .slide-body strong { font-weight: 700; }
  .team-photo {
    position: absolute;
    left: 690px; top: 180px;
    width: 300px;
    height: 250px;
    background: linear-gradient(160deg, var(--photo-a), var(--photo-b));
    border-radius: 4px;
  }
  .rule-orange {
    position: absolute;
    left: 0; top: 528px;
    width: 100%;
    height: 5px;
    background: var(--orange);
  }
  .rule-navy {
    position: absolute;
    left: 0; bottom: 0;
    width: 100%;
    height: 18px;
    background: var(--navy);
  }
</style>
</head>
<body>
  <section class="slide">
    <header class="slide-header">
      <h1 class="slide-title">Título do Slide</h1>
      <p class="slide-subtitle">subtítulo (se houver)</p>
      <div class="brand"><span class="brand-dot"></span>Clarvia Serviços</div>
    </header>

    <p class="slide-body">
      Lorem ipsum dolor sit amet, enim arcu quam, maecenas
      dolor consectetuer wisi neque wisi mauris, facilisis sit dolores orci
      mauris, turpis lacus fringilla erat elit, sit duis nunc aut ut vitae. Sed
      molestie eu lorem, arcu faucibus fringilla sagittis arcu dolor. Amet sapien
      ut tempor vulputate, <strong>viverra id volutpat ac turpis</strong>, aliquam tellus, magna
      sed iaculis pellentesque. Eget vulputate egestas nostra magnis mi,
      lobortis quam commodo, a ornare, convallis eu.
    </p>

    <div class="team-photo" role="img" aria-label="Foto da equipe de limpeza uniformizada com carrinhos e materiais de limpeza"></div>

    <div class="rule-orange"></div>
    <div class="rule-navy"></div>
  </section>
</body>
</html>
```